Business Card Design

We need a business card designed to portray the message that we are wedding and event stylists. We set up garden ceremonies and style wedding reception venues with chair covers and sashes, backdrops and draping's, wishing wells, tealight holders, table centerpieces. We also style corporate functions - Christmas parties, gala dinners, school formals, award nights. The colour of our uniforms are black and hot pink, if these colours could be incorporated. We would like to be able to use this design for letterhead, flyers and postcards etc. We would like the design to portray a professional, classic image that would relate to both spectrums of our business, weddings and corporate events. If you could develop a logo to incorporate would be great

Target Market(s)

brides, corporate compaines

Industry/Entity Type

Wedding

Contact Information for Business Card

Velvet Crest Occasions & Party Hire
Phone: 0417 553 916 Email:vcoph@fernmail.example
Web: www.velvetcrestoccasions.example.au

Requirements
Must have
• Must include that we set up for weddings, engagements, birthdays, anniversaries, corporate functions, school formals, any occasion.

```html
<!DOCTYPE html>
<html lang="en">
<head>
<meta charset="utf-8">
<title>Velvet Crest Occasions and Party Hire – Business Card</title>
<link rel="stylesheet" href="https://fonts.googleapis.com/css2?family=Tinos:ital,wght@1,400&display=swap">
<style>
  :root {
    --page: #ffffff;
    --card-edge: #b4879a;
    --card-glow: #f1dde7;
    --ink: #9a5b79;
    --ink-deep: #8a4c6a;
    --ornament: #f7ecf1;
    --serif: "Tinos", "Times New Roman", serif;
  }
  * { box-sizing: border-box; margin: 0; padding: 0; }
  html, body {
    width: 1200px; height: 1000px; overflow: hidden;
    background: var(--page);
  }
  .card {
    position: absolute; left: 78px; top: 162px;
    width: 1080px; height: 653px;
    border-radius: 22px;
    background: var(--card-glow);
    box-shadow: inset 0 0 45px 42px var(--card-edge);
    font-family: var(--serif);
    font-style: italic;
    color: var(--ink);
    text-align: center;
  }
  .ornament {
    position: absolute; top: 30px; width: 230px; height: 600px;
    border-radius: 40px;
    background: radial-gradient(ellipse at center, rgba(247,236,241,0.55), rgba(247,236,241,0) 70%);
  }
  .ornament--left { left: 25px; }
  .ornament--right { right: 25px; }
  .card__name {
    position: absolute; left: 0; right: 0; top: 92px;
    font-size: 52px; font-weight: 400;
    color: var(--ink);
    text-shadow: 1px 2px 2px rgba(110,50,80,0.45), -1px -1px 0 rgba(255,255,255,0.6);
  }
  .services {
    position: absolute; left: 0; right: 0; top: 194px;
    list-style: none;
    font-size: 35px; line-height: 42px;
  }
  .services__mark { font-style: normal; font-size: 24px; vertical-align: 4px; margin-right: 4px; }
  .contact {
    position: absolute; left: 0; right: 0; top: 474px;
    font-size: 28px; line-height: 33px;
    color: var(--ink-deep);
  }
  .contact__label { text-decoration: underline; text-underline-offset: 4px; }
  .contact__gap { display: inline-block; width: 28px; }
</style>
</head>
<body>
  <section class="card" aria-label="Business card">
    <div class="ornament ornament--left" role="img" aria-label="Pale swirl, heart and butterfly flourish"></div>
    <div class="ornament ornament--right" role="img" aria-label="Pale swirl, heart and butterfly flourish"></div>

    <h1 class="card__name">Velvet Crest Occasions and Party Hire</h1>

    <ul class="services">
      <li><span class="services__mark">♦</span>Weddings&nbsp; <span class="services__mark">♦</span>Engagements&nbsp; <span class="services__mark">♦</span>Anniversaries</li>
      <li><span class="services__mark">♦</span>Birthdays&nbsp; <span class="services__mark">♦</span>School Formals</li>
      <li><span class="services__mark">♦</span>Corporate Functions</li>
      <li><span class="services__mark">♦</span>Any occasion</li>
      <li>big or small</li>
    </ul>

    <address class="contact">
      <span class="contact__label">Phone</span>: 0417 553 916<span class="contact__gap"></span><span class="contact__label">Email</span>:vcoph@fernmail.example<br>
      <span class="contact__label">Web</span>: www.velvetcrestoccasions.example.au
    </address>
  </section>
</body>
</html>
```